Clinician Supply Circle

I am a financial planner whose client's are physicians and dentists. As physicians, there is very little time for them to do research on numerous aspects of their business and personal lives. I am looking to build a website that is a 1 stop shop for many of the services/resources they may need. It will be my job to screen the resources/advertisers and place competent people/business's that I know and have a track record on. there will ultimately be 10 or 12 ish areas that I would like to provide resources in:
disability insurance
life insurance
retirement planning
student loan advisors
employment contract and business formation attorneys
accountants
real estate agents
physician mortgages
personal loans
malpractice insurance
physician recruiters
maybe 2 other areas which I have yet to figure out.....
I would like each of these options to be able to be clicked on and a page will open up with the 1 or 2 or 3 or 4 people/business's that I have picked to represent these areas. I would like each specific person/business to have a click here to contact me link in which an email goes to the person and I am copied on the initial correspondence between the physician and the mortgage broker.... just so I can see some of the correspondence they will be receiving.
nowhere on the site do I want it to say my name. there will be certain disclosures that are needed and other wording but I think this is a good starting point.
here are links to two websites with the same general concept. please keep in mind that I want my website to be more on the simple side.
http://www.quillbarrowpartners.example/index.html
http://fernlakeledger.example/
Updates
Industry/Entity Type
Financial

```html
<!DOCTYPE html>
<html lang="en">
<head>
<meta charset="utf-8">
<title>Clinician Supply Circle</title>
<link href="https://fonts.googleapis.com/css2?family=Varela+Round&family=Open+Sans:wght@400;600&display=swap" rel="stylesheet">
<style>
:root{
  --blue:#1a9ad6;
  --blue-dark:#0f6fae;
  --blue-light:#35b6ee;
  --sky:#12a3e3;
  --orange:#f7a025;
  --orange-dark:#f08a12;
  --ink:#333;
  --grey:#777;
  --grey-light:#9a9a9a;
  --line:#e2e2e2;
  --panel:#f6f6f6;
  --white:#fff;
}
*{box-sizing:border-box;margin:0;padding:0}
html,body{width:711px;height:1200px;overflow:hidden;background:var(--white)}
body{font-family:"Open Sans",sans-serif;color:var(--ink)}
.page{position:relative;width:711px;height:1200px;border-top:2px solid var(--blue)}
.abs{position:absolute}
.heading{font-family:"Varela Round",sans-serif;color:var(--blue);font-weight:400}

.brand{left:52px;top:24px;font-family:"Varela Round",sans-serif;font-size:15px;color:var(--blue);display:flex;align-items:center;gap:6px}
.brand-dot{width:10px;height:10px;background:var(--orange);border-radius:50%}
.appointment{right:53px;top:22px;text-align:right;font-family:"Varela Round",sans-serif;color:var(--blue-dark)}
.appointment small{display:block;font-size:10px}
.appointment strong{display:block;font-size:18px;font-weight:400;margin-top:1px}

.main-nav{left:53px;top:72px;width:605px;height:31px;background:linear-gradient(var(--blue-light),var(--blue));border-radius:3px 3px 0 0;display:flex}
.main-nav a{color:var(--white);font-size:8px;font-weight:600;text-decoration:none;display:flex;align-items:center;justify-content:center;border-right:1px solid rgba(0,0,0,.15)}
.main-nav a:last-child{border-right:0}

.hero{left:53px;top:103px;width:605px;height:238px;border-radius:0 0 3px 3px;overflow:hidden;background:linear-gradient(90deg,#3a3a3a,#555 55%,#444)}
.hero-photo{position:absolute;right:40px;top:0;width:260px;height:238px;background:radial-gradient(ellipse at 55% 45%,#e9e6e3,#bdb7b2 55%,transparent 75%)}
.hero-circle{position:absolute;left:15px;top:28px;width:196px;height:196px;border-radius:50%;background:rgba(20,130,190,.88);text-align:center;color:var(--white);padding-top:46px}
.hero-circle h1{font-family:"Varela Round",sans-serif;font-weight:400;font-size:16px;line-height:20px;padding:0 20px}
.hero-circle p{font-size:7.2px;line-height:11px;margin:8px 22px 0}
.dots{display:flex;justify-content:center;gap:3px;margin-top:10px}
.dots i{width:6px;height:6px;border-radius:50%;background:rgba(255,255,255,.5)}
.dots i:first-child{background:var(--white)}

.feature{top:364px;display:flex;gap:10px;width:190px}
.feature svg{flex:none}
.feature h3{font-size:13px;margin-bottom:4px}
.feature p{font-size:7.4px;line-height:13px;color:var(--grey-light)}
.divider{left:53px;top:450px;width:605px;height:1px;background:var(--line)}

.welcome-title{left:53px;top:482px;font-size:17.5px}
.welcome-lead{left:53px;top:512px;width:392px;font-size:8.8px;line-height:14px;color:#555}
.welcome-body{left:53px;top:547px;width:392px;font-size:7.4px;line-height:14.4px;color:#555}
.welcome-photo{left:460px;top:478px;width:196px;height:116px;border:1px solid #d6d6d6;padding:4px;background:var(--white)}
.fill{width:100%;height:100%}

.adviser-title{left:53px;top:620px;font-size:15px}
.adviser-card{top:651px;width:184px}
.adviser-card .fill{height:74px}
.adviser-card h4{font-size:8.8px;font-weight:400;margin:10px 0 4px 2px}
.adviser-card p{font-size:7px;line-height:14px;color:var(--grey);margin-left:2px}
.btn{display:inline-block;margin-top:7px;width:74px;height:21px;line-height:21px;text-align:center;background:linear-gradient(var(--orange),var(--orange-dark));color:var(--white);font-size:7.4px;border-radius:3px}

.services{left:489px;top:622px;width:167px;height:200px;border-radius:6px;overflow:hidden;background:linear-gradient(var(--sky),var(--blue-dark))}
.services h3{height:27px;background:var(--orange);color:var(--white);font-family:"Varela Round",sans-serif;font-weight:400;font-size:13px;padding:5px 9px}
.services ul{list-style:none;padding:8px 8px 0 22px}
.services li{position:relative;color:var(--white);font-size:7.3px;line-height:13px}
.services li::before{content:"";position:absolute;left:-8px;top:4.5px;border:2px solid transparent;border-left:3px solid rgba(255,255,255,.8)}

.blog-title{left:53px;top:840px;font-size:15px}
.blog-arrows{left:640px;top:843px}
.blog-card{top:871px;width:288px;height:151px;border:1px solid #ddd;background:var(--panel)}
.blog-card .thumb{position:absolute;left:6px;top:10px;width:133px;height:105px}
.blog-card .body{position:absolute;left:146px;top:16px;width:133px}
.blog-card h4{font-size:7.6px;font-weight:600;color:#222;margin-bottom:4px}
.blog-card p{font-size:6.4px;line-height:10.6px;color:#555;text-align:justify}
.blog-actions{position:absolute;left:0;bottom:0;width:100%;height:25px;border-top:1px solid #ddd;display:flex;background:var(--white)}
.blog-actions span{flex:1;display:flex;align-items:center;justify-content:center;gap:4px;font-size:7px;color:#444;border-right:1px solid #ddd}
.blog-actions span:last-child{border-right:0}
.blog-actions i{width:7px;height:6px;background:var(--blue-dark);border-radius:1px}

.testimonials-title{left:53px;top:1041px;font-size:15px}
.quote{top:1068px;width:280px}
.quote .mark{position:absolute;font-family:Georgia,serif;font-size:20px;color:#555;line-height:1}
.quote p{font-size:7.2px;line-height:14px;color:#333;padding-left:18px}
.quote cite{display:block;text-align:right;font-size:6.8px;font-style:italic;margin-top:2px;padding-right:10px}

.footer{left:0;top:1138px;width:711px;height:62px;background:var(--sky);color:var(--white)}
.footer nav{position:absolute;left:59px;top:18px;font-size:6.8px}
.footer small{position:absolute;left:59px;top:32px;font-size:6.8px}
.social{position:absolute;left:581px;top:26px;display:flex;gap:5px}
.social i{width:14px;height:14px;background:var(--blue-dark);border-radius:2px}
.social i:last-child{background:var(--orange)}
</style>
</head>
<body>
<div class="page">

  <div class="abs brand"><span class="brand-dot"></span>Clinician Supply Circle</div>
  <div class="abs appointment"><small>Make an Appointment</small><strong>555.014.2930</strong></div>

  <nav class="abs main-nav">
    <a style="width:71px">Home</a><a style="width:72px">About Us</a><a style="width:70px">Services</a>
    <a style="width:86px">Investments</a><a style="width:70px">Medical</a><a style="width:64px">Adviser</a>
    <a style="width:65px">Blog</a><a style="width:107px">Contatc Us</a>
  </nav>

  <section class="abs hero">
    <div class="hero-photo" role="img" aria-label="Smiling doctor in a white coat with a stethoscope against a chalkboard"></div>
    <div class="hero-circle">
      <h1>Clinician Supply Circle</h1>
      <p>Cum sociis natoque penatibus et magnis dis parturient montes nascetur ridiculus mus In iaculis facilisis massa</p>
      <div class="dots"><i></i><i></i><i></i><i></i></div>
    </div>
  </section>

  <div class="abs feature" style="left:74px">
    <svg width="38" height="46" viewBox="0 0 38 46"><circle cx="19" cy="10" r="8" fill="#666"/><path d="M3 44v-12c0-8 7-12 16-12s16 4 16 12v12z" fill="#666"/><path d="M15 20l4 10 4-10" fill="#fff"/></svg>
    <div><h3 class="heading">Meet Our Adviser</h3><p>Vestibulum ligula augue bibendum accumsan vestibulum ut commodo a mi Morbi Curabitur iaculis</p></div>
  </div>
  <div class="abs feature" style="left:276px">
    <svg width="34" height="48" viewBox="0 0 34 48"><circle cx="21" cy="6" r="5" fill="#666"/><path d="M18 13l-7 13 8 5-4 14M18 13l6 10 7 1M14 20l-9 2M19 31l-10 8" stroke="#666" stroke-width="5" fill="none" stroke-linecap="round"/></svg>
    <div><h3 class="heading">Services Provide</h3><p>Vestibulum ligula augue bibendum accumsan vestibulum ut commodo a mi Morbi Curabitur iaculis</p></div>
  </div>
  <div class="abs feature" style="left:472px">
    <svg width="46" height="46" viewBox="0 0 46 46"><path d="M2 42l6-14h30l6 14z" fill="none" stroke="#777" stroke-width="1.5"/><path d="M23 34c-8-10-11-15-11-20a11 11 0 0 1 22 0c0 5-3 10-11 20z" fill="#666"/><circle cx="23" cy="14" r="4" fill="#fff"/></svg>
    <div><h3 class="heading">Our Location</h3><p>Vestibulum ligula augue bibendum accumsan vestibulum ut commodo a mi Morbi Curabitur iaculis</p></div>
  </div>

  <div class="abs divider"></div>

  <h2 class="abs heading welcome-title">Welcome To Our Company</h2>
  <p class="abs welcome-lead">Donec scelerisque leo ac risus Praesent sit amet est In dictum dolor eu dictum porttitor enim felis viverra mi eget luctus massa purus quis odio Etiam nulla massa</p>
  <p class="abs welcome-body">Aliquam nec erat at purus cursus interdum Vestibulum ligula augue bibendum accumsan vestibulum ut commodo a mi Morbi ornare gravida elit Integer congue augue et malesuada iaculis ipsum dui aliquet felis at cursus magna nisl nec elit Praesent elementum elit at tellus nec ultricies sit amet porttitor mattis enim</p>
  <div class="abs welcome-photo"><div class="fill" role="img" aria-label="Dental team with a patient in a bright clinic" style="background:linear-gradient(120deg,#b9d7ee,#6fa6d3 50%,#dfe9f2)"></div></div>

  <h2 class="abs heading adviser-title">Physicians &amp; Dentists Adviser</h2>
  <div class="abs adviser-card" style="left:55px">
    <div class="fill" role="img" aria-label="Hands examining a patient's elbow" style="background:linear-gradient(120deg,#9fb4cc,#e8c8b4 55%,#c9d3df)"></div>
    <h4>Nunc tempus felis vitae urna</h4>
    <p>Vivamus porttitor g puttrus nisi eleifend libero a tempus libero lectus feugiat felis Morbi diam</p>
    <span class="btn">READ MORE</span>
  </div>
  <div class="abs adviser-card" style="left:266px">
    <div class="fill" role="img" aria-label="Physiotherapist stretching a patient's leg" style="background:linear-gradient(120deg,#eceff1,#e3cbb8 50%,#2c3550 80%)"></div>
    <h4>Curabitur iaculis tempus eros</h4>
    <p>Vivamus porttitor g puttrus nisi eleifend libero a tempus libero lectus feugiat felis Morbi diam</p>
    <span class="btn">READ MORE</span>
  </div>

  <aside class="abs services">
    <h3>Services</h3>
    <ul>
      <li>Disability insurance</li><li>life insurance</li><li>Retirement planning</li><li>Student loan advisors</li>
      <li>Employment contract and business formation attorneys</li><li>Accountants</li><li>Real estate agents</li>
      <li>Physician mortgages</li><li>Personal loans</li><li>Malpractice insurance</li><li>Physician recruiters</li>
    </ul>
  </aside>

  <h2 class="abs heading blog-title">Blog</h2>
  <svg class="abs blog-arrows" width="16" height="10" viewBox="0 0 16 10"><path d="M5 1L1 5l4 4M11 1l4 4-4 4" stroke="#111" stroke-width="1.6" fill="none"/></svg>

  <article class="abs blog-card" style="left:54px">
    <div class="thumb" role="img" aria-label="Watercolour illustration of a nurse caring for a patient" style="background:linear-gradient(135deg,#3aa7d8,#e8d36a 50%,#f4f0e6)"></div>
    <div class="body"><h4>Lorem ipsum dolor sit amet</h4><p>Nam justo nulla, pharetra consectetur molestie in, pellentesque in risus. Nunc tincidunt risus id neque suscipit at venenatis leo sagittis. Quisque elementum, dolor quis imperdiet vestibulum, urna justo convallis magna, at bibendum est purus eget tellus.</p></div>
    <div class="blog-actions"><span><i></i>Email Friends</span><span><i></i>Print</span><span><i></i>Comments</span><span><i></i>Like</span></div>
  </article>
  <article class="abs blog-card" style="left:369px">
    <div class="thumb" role="img" aria-label="Doctor reviewing paperwork with an older patient" style="background:linear-gradient(135deg,#c9d7e2,#f1ece7 50%,#9fb1c1)"></div>
    <div class="body"><h4>Lorem ipsum dolor sit amet</h4><p>Nam justo nulla, pharetra consectetur molestie in, pellentesque in risus. Nunc tincidunt risus id neque suscipit at venenatis leo sagittis. Quisque elementum, dolor quis imperdiet vestibulum, urna justo convallis magna, at bibendum est purus eget tellus.</p></div>
    <div class="blog-actions"><span><i></i>Email Friends</span><span><i></i>Print</span><span><i></i>Comments</span><span><i></i>Like</span></div>
  </article>

  <h2 class="abs heading testimonials-title">Testimonials</h2>
  <blockquote class="abs quote" style="left:54px">
    <span class="mark" style="left:4px;top:-2px">&ldquo;</span>
    <p>Lorem ipsum dolor sit amet, consectetuer adipiscing elit. Aenean commodo ligula eget dolor. Aenean massa. Cum sociis natoque penatibus et</p>
    <cite>-Harlan Voss, CEO</cite>
    <span class="mark" style="right:-6px;top:40px">&rdquo;</span>
  </blockquote>
  <blockquote class="abs quote" style="left:360px">
    <span class="mark" style="left:2px;top:-2px">&ldquo;</span>
    <p>Lorem ipsum dolor sit amet, consectetuer adipiscing elit. Aenean commodo ligula eget dolor. Aenean massa. Cum sociis natoque penatibus et</p>
    <cite>-Harlan Voss, CEO</cite>
    <span class="mark" style="right:-6px;top:40px">&rdquo;</span>
  </blockquote>

  <footer class="abs footer">
    <nav>Home &nbsp;|&nbsp; About Us &nbsp;|&nbsp; Products &nbsp;|&nbsp; Contact Us</nav>
    <small>&copy; 2014 Company Name &nbsp;All right reserved &nbsp;Term of Use</small>
    <div class="social"><i></i><i></i><i></i><i></i></div>
  </footer>

</div>
</body>
</html>
```